Educational Software Company Seeking Event Postcard Design

We are looking for a postcard promoting an upcoming event. We would like to utilize the red, white and blue color scheme that you will see on the site at: http://plantstewards.campuswren.example/ksq. Gray can also be used. Please feel free to add some extra design elements. This postcard is targeting education operations professionals.

7th Annual Upper Granite Coast Grounds Stewards Summit

When: February 27th -28th

Where: Portsmouth, New Hampshire

Call to action - Register Today: linkbrief.example/GSS-Register

I have attached a word containing the text I'd like you to use and an example template. Some design elements will need to be added to the template

Red = bf1e2d
Blue = 0054a6

Target Market(s)

education operations professionals

Industry/Entity Type

Education

Requirements
Must have
• Grounds Stewards Summit logo, name of conference, date, location, blue, red, white and gray seen on website:

Red = bf1e2d
Blue = 0054a6

When: February 27th -28th

Please see attached word document called 2014_GSS_UGC Postcard for content.

```html
<!DOCTYPE html>
<html lang="en">
<head>
<meta charset="utf-8">
<title>Grounds Stewards Summit – Postcard</title>
<link rel="stylesheet" href="https://fonts.googleapis.com/css2?family=Cinzel:wght@400&family=Open+Sans:wdth,wght@75..100,300..800&display=swap">
<style>
  :root {
    --paper: #ffffff;
    --ink-gray: #5a5a5a;
    --brand-red: #bf1e2d;
    --band-red: #cc2f48;
    --brand-blue: #0054a6;
    --text-white: #ffffff;
  }
  html, body {
    margin: 0;
    padding: 0;
    overflow: hidden;
    background: var(--paper);
  }
  .postcard {
    position: relative;
    width: 1200px;
    height: 773px;
    background: var(--paper);
    overflow: hidden;
  }
  .event-mark {
    position: absolute;
    left: 50%;
    top: 38px;
    width: 220px;
    height: 220px;
    margin-left: -110px;
    box-sizing: border-box;
    border: 8px solid var(--brand-blue);
    border-radius: 50%;
    display: flex;
    align-items: center;
    justify-content: center;
  }
  .event-mark-name {
    font-family: "Cinzel", serif;
    font-weight: 400;
    font-size: 70px;
    color: var(--brand-red);
    letter-spacing: 2px;
  }
  .event-title {
    position: absolute;
    left: 0;
    right: 0;
    top: 330px;
    margin: 0;
    text-align: center;
    font-family: "Cinzel", serif;
    font-weight: 400;
    font-size: 50px;
    line-height: 64px;
    color: var(--ink-gray);
    letter-spacing: 1px;
  }
  .event-title span { display: block; }
  .event-when-where {
    position: absolute;
    left: 0;
    right: 0;
    top: 538px;
    margin: 0;
    text-align: center;
    font-family: "Open Sans", sans-serif;
    font-stretch: 80%;
    font-weight: 400;
    font-size: 31px;
    color: var(--brand-red);
  }
  .register-band {
    position: absolute;
    left: 0;
    right: 0;
    top: 627px;
    height: 84px;
    background: var(--band-red);
    display: flex;
    align-items: center;
    justify-content: center;
  }
  .register-call {
    margin: 0;
    font-family: "Open Sans", sans-serif;
    font-stretch: 75%;
    font-weight: 700;
    font-size: 44px;
    color: var(--text-white);
  }
</style>
</head>
<body>
  <main class="postcard">
    <div class="event-mark">
      <span class="event-mark-name">GSS</span>
    </div>
    <h1 class="event-title">
      <span>7th Annual</span>
      <span>Upper Granite Coast</span>
      <span>Grounds Stewards Summit</span>
    </h1>
    <p class="event-when-where">February 27th -28th in Portsmouth, New Hampshire</p>
    <div class="register-band">
      <p class="register-call">Register Today : linkbrief.example/GSS-Register</p>
    </div>
  </main>
</body>
</html>
```